Self Defence Seminar Flyer

Need a flyer that will sell a seminar that will teach self defence techniques to customers. Needs to have a good image that will remind people about the dangerous world. The seminar is for men and women.

Needs to look professional.

I have attached the previous flyer we used. needs same information except without the same date and time for seminar.

Target Market(s)

Male and Females interested in learning how to defend themselves or family

Industry/Entity Type

Defence

Requirements
Must have
• A Image that reminds people of a dangerous situation

```html
<!DOCTYPE html>
<html lang="en">
<head>
<meta charset="UTF-8">
<title>Self Defence Seminar Flyer</title>
<link rel="stylesheet" href="https://fonts.googleapis.com/css2?family=Fjalla+One&family=Oswald:wght@300;400&display=swap">
<style>
  :root {
    --teal: #7dd5c3;
    --teal-light: #a6e4d6;
    --teal-deep: #5cc3ae;
    --swoosh: #ffffff;
    --line-green: #1b9676;
    --line-yellow: #f2da80;
    --text: #ffffff;
    --label: #f3df8a;
    --scene-top: #8fcfc2;
    --scene-mid: #8a9aa3;
    --scene-low: #4b5663;
  }
  html, body {
    margin: 0;
    padding: 0;
    width: 847px;
    height: 1200px;
    overflow: hidden;
    background: var(--teal);
  }
  .flyer {
    position: relative;
    width: 847px;
    height: 1200px;
    overflow: hidden;
    background:
      radial-gradient(ellipse 420px 520px at 120px 330px, rgba(255,255,255,0.18), transparent 70%),
      radial-gradient(ellipse 300px 420px at 760px 420px, rgba(255,255,255,0.12), transparent 70%),
      radial-gradient(ellipse 380px 300px at 200px 1050px, rgba(0,80,60,0.10), transparent 70%),
      linear-gradient(160deg, var(--teal-light) 0%, var(--teal) 45%, var(--teal-deep) 100%);
  }
  .street-scene {
    position: absolute;
    left: 440px;
    top: 700px;
    width: 407px;
    height: 500px;
    background: linear-gradient(180deg, var(--scene-top) 0%, var(--scene-mid) 30%, var(--scene-low) 100%);
    -webkit-mask-image: linear-gradient(180deg, transparent 0%, #000 22%);
    mask-image: linear-gradient(180deg, transparent 0%, #000 22%);
  }
  .swoosh {
    position: absolute;
    inset: 0;
    width: 847px;
    height: 1200px;
  }
  .pitch {
    position: absolute;
    left: 27px;
    top: 14px;
    width: 490px;
    margin: 0;
    font-family: "Fjalla One", "Arial Narrow", sans-serif;
    font-size: 19.5px;
    line-height: 23.5px;
    letter-spacing: 0.4px;
    color: var(--text);
    text-shadow: 0 1px 2px rgba(0,60,50,0.25);
  }
  .pitch p { margin: 0 0 24px; }
  .event-details {
    position: absolute;
    left: 640px;
    top: 350px;
    width: 190px;
    margin: 0;
    padding: 0;
    list-style: none;
    font-family: "Oswald", "Arial Narrow", sans-serif;
    font-weight: 300;
    font-size: 27px;
    color: var(--label);
    text-align: center;
  }
  .event-details li { height: 82px; }
</style>
</head>
<body>
  <main class="flyer">
    <div class="street-scene" role="img" aria-label="Photo of a woman looking over her shoulder at a hooded man following her on a city street"></div>

    <svg class="swoosh" viewBox="0 0 847 1200" aria-hidden="true">
      <path fill="var(--swoosh)" d="M742 0 C560 200 380 470 372 760 C368 930 420 1090 470 1200 L540 1200 C470 1040 455 850 505 640 C560 400 700 170 847 30 L847 0 Z"/>
      <path fill="none" stroke="var(--line-yellow)" stroke-width="3" d="M812 0 C650 170 520 390 500 600 C490 720 495 820 505 900"/>
      <path fill="none" stroke="var(--line-green)" stroke-width="6" d="M847 40 C660 200 520 420 492 640 C470 830 500 1030 545 1200"/>
    </svg>

    <section class="pitch">
      <p>Being a victim is a topic that people to avoid . un-fortunatley we live in an increasingly dangerous society for men and women alike learning to defend yourself is an imporatant life skill.</p>
      <p>Spend 2 hours with us learing some simple and effective self defence tactics that one day may be needed to defend yourself or loved ones</p>
      <p>Our aim is to teach you effcective and efficient technquies and tactics to be able to defend yourself in a range of sitatuions</p>
      <p>Learn the same techniques and tactics that we have taught to individuals in law enforcment security and military. We incorporate weapon defence use of surroundings and psychological techniques in our classes</p>
    </section>

    <ul class="event-details">
      <li>DATE :</li>
      <li>LOCATION</li>
      <li>WEBSITE</li>
    </ul>
  </main>
</body>
</html>
```